Tarvin Group Business Card

Building Management company based in Sydney, Australia. We provide onsite management for commercial and residential buildings.
I would like a sophisticated minimalist design that indicates that we provide a high-end service. I would like a silver or metal look background or something similar.
The business card should have:
Name
Title
email
Office Phone
Mobile
Address
Website
The services that we provide should be prominent:
Building Management - Concierge - Caretaking - Cleaning

```html
<!DOCTYPE html>
<html lang="en">
<head>
<meta charset="utf-8">
<title>Tarvin Group Business Card</title>
<link rel="stylesheet" href="https://fonts.googleapis.com/css2?family=Open+Sans:wght@400;600;700&display=swap">
<style>
  :root {
    --backdrop: #2b2c2e;
    --metal-light: #f4f5f6;
    --metal-mid: #dcdee0;
    --metal-dark: #c4c7ca;
    --brand-blue: #2a6fc0;
    --ink: #1b1c1e;
    --ink-soft: #3a3b3d;
  }
  * { box-sizing: border-box; margin: 0; padding: 0; }
  html, body {
    width: 1200px; height: 852px; overflow: hidden;
    background: var(--backdrop);
    font-family: "Open Sans", Arial, sans-serif;
  }
  .stage {
    width: 1200px; height: 852px;
    display: flex; align-items: center; justify-content: center; gap: 40px;
  }
  .card {
    position: relative;
    width: 540px; height: 310px;
    border-radius: 22px;
    overflow: hidden;
    background:
      linear-gradient(115deg, rgba(255,255,255,0.55) 0%, rgba(255,255,255,0) 35%, rgba(255,255,255,0.35) 60%, rgba(255,255,255,0) 85%),
      linear-gradient(180deg, var(--metal-light) 0%, var(--metal-mid) 55%, var(--metal-dark) 100%);
  }
  .wordmark {
    display: flex; align-items: center; gap: 12px;
    font-weight: 700; color: var(--ink);
    letter-spacing: 1px; text-transform: uppercase;
  }
  .wordmark__square { background: var(--brand-blue); flex: none; }

  /* Front */
  .card--front .wordmark {
    position: absolute; left: 0; right: 0; top: 92px;
    justify-content: center; font-size: 38px;
  }
  .card--front .wordmark__square { width: 30px; height: 30px; }
  .front__rule {
    position: absolute; height: 2px; width: 60px; background: var(--brand-blue);
  }
  .front__rule--upper { left: 372px; top: 164px; }
  .front__rule--lower { left: 108px; top: 220px; }
  .front__web {
    position: absolute; left: 0; right: 0; top: 186px;
    text-align: center; font-size: 14px; letter-spacing: 3px; color: var(--ink-soft);
  }
  .front__services {
    position: absolute; left: 0; right: 0; top: 244px;
    text-align: center; font-size: 12px; font-weight: 600;
    letter-spacing: 1.5px; text-transform: uppercase; color: var(--brand-blue);
  }

  /* Back */
  .back__stripe {
    position: absolute; left: 0; top: 0; bottom: 0; width: 8px;
    background: var(--brand-blue);
  }
  .card--back .wordmark {
    position: absolute; right: 36px; top: 56px; font-size: 26px; gap: 10px;
  }
  .card--back .wordmark__square { width: 22px; height: 22px; }
  .holder { position: absolute; left: 44px; top: 92px; }
  .holder__name { font-size: 17px; font-weight: 700; color: var(--brand-blue); }
  .holder__title { font-size: 11px; color: var(--ink-soft); margin-top: 2px; padding-left: 14px; }
  .contacts {
    position: absolute; left: 44px; bottom: 32px;
    list-style: none; font-size: 13px; color: var(--ink); line-height: 19px;
  }
  .contacts__item { display: flex; align-items: flex-start; gap: 10px; }
  .contacts__icon { width: 12px; height: 12px; margin-top: 4px; flex: none; fill: var(--ink-soft); }
  .contacts__gap { padding-left: 22px; }
</style>
</head>
<body>
<main class="stage">
  <section class="card card--front" aria-label="Card front">
    <div class="wordmark"><span class="wordmark__square"></span><span>Tarvin Group</span></div>
    <span class="front__rule front__rule--upper"></span>
    <p class="front__web">www.tarvingroup.com.au</p>
    <span class="front__rule front__rule--lower"></span>
    <p class="front__services">Building Management · Concierge · Caretaking · Cleaning</p>
  </section>

  <section class="card card--back" aria-label="Card back">
    <span class="back__stripe"></span>
    <div class="holder">
      <p class="holder__name">Your Long Name</p>
      <p class="holder__title">Managing Director</p>
    </div>
    <div class="wordmark"><span class="wordmark__square"></span><span>Tarvin Group</span></div>
    <ul class="contacts">
      <li class="contacts__item">
        <svg class="contacts__icon" viewBox="0 0 12 12"><path d="M1 3c0-1 1-2 2-2h6c1 0 2 1 2 2v1H8V3H4v1H1z M2 5h8l1 5H1z"/></svg>
        <span>00.00.00.0000</span>
      </li>
      <li class="contacts__item">
        <svg class="contacts__icon" viewBox="0 0 12 12"><path d="M3 0h6v12H3z M4 1v8h4V1z"/></svg>
        <span>00.00.00.0000</span>
      </li>
      <li class="contacts__item">
        <svg class="contacts__icon" viewBox="0 0 12 12"><path d="M0 2h12v8H0z M1 3l5 4 5-4z" fill-rule="evenodd"/></svg>
        <span>yourname@yourwebsite.com</span>
      </li>
      <li class="contacts__item">
        <svg class="contacts__icon" viewBox="0 0 12 12"><circle cx="6" cy="6" r="5.5"/><path d="M0.5 6h11M6 0.5v11" stroke="#dcdee0" stroke-width="1"/></svg>
        <span>www.yourwebsite.com</span>
      </li>
      <li class="contacts__gap">Your Commercial or office address<br>in just two line with pincode</li>
    </ul>
  </section>
</main>
</body>
</html>
```